Bref créative
Varneth Systems Stationery
Business card, envelops and letterhead
Bright & Fun-filled
Dorian Kelbrook
President & Chief Architect
418 W. Harrow Ln.
Kent, WA 98047
dorian.kelbrook@varneth.example
http://www.varneth.example
Please provide duplicate ai files in Illustrator 8.0 format and simlilar lower versions of any other files you provide as well as the originals
Logo only (without name)
Tag line:
"Providing Enterprise Business Solutions"
Original AI files

```html
<!DOCTYPE html>
<html lang="en">
<head>
<meta charset="utf-8">
<title>Varneth Systems Stationery</title>
<link rel="stylesheet" href="https://fonts.googleapis.com/css2?family=Montserrat:wght@400;600;700&family=Open+Sans:wght@400;600&display=swap">
<style>
  :root{
    --backdrop:#e7e3dd;
    --paper:#ffffff;
    --navy:#1f2c6e;
    --ink:#14161c;
    --grey:#6d7078;
    --rule:#b9bcc4;
    --faint:#eef0f4;
    --card-dark:#2e3035;
  }
  *{box-sizing:border-box;margin:0;padding:0}
  html,body{width:1200px;height:540px;overflow:hidden}
  body{background:var(--backdrop);position:relative;font-family:"Open Sans",Arial,sans-serif;color:var(--ink)}

  .sheet,.envelope,.card{position:absolute;background:var(--paper);box-shadow:0 2px 8px rgba(0,0,0,.18);overflow:hidden}

  .brand{position:absolute;display:flex;align-items:center;gap:6px}
  .brand-dot{width:16px;height:16px;border-radius:50%;background:var(--navy)}
  .brand-name{font-family:"Montserrat",Arial,sans-serif;font-weight:700;color:var(--navy);font-size:14px;letter-spacing:.5px;text-transform:uppercase;line-height:1}

  .contact{position:absolute;font-size:5.5px;line-height:8px;color:var(--grey);text-align:left}
  .wave{position:absolute;left:0;bottom:0;width:100%}
  .footer-text{position:absolute;color:#fff;font-size:5px;line-height:7px;text-align:right}
  .tagline{position:absolute;color:#fff;font-family:"Montserrat",Arial,sans-serif;font-size:7px;font-weight:600}

  /* letterhead */
  .letterhead{left:12px;top:19px;width:336px;height:504px}
  .letterhead .brand{left:20px;top:18px}
  .watermark{position:absolute;left:120px;top:160px;width:96px;height:96px;border-radius:50%;background:var(--faint)}

  /* fax */
  .fax{left:372px;top:19px;width:336px;height:504px}
  .fax .brand{left:20px;top:18px}
  .fax .contact{left:246px;top:16px}
  .fax-title{position:absolute;left:22px;top:126px;font-family:"Montserrat",Arial,sans-serif;font-size:26px;font-weight:400;letter-spacing:1px}
  .fax-fields{position:absolute;left:22px;top:168px;width:292px;display:grid;grid-template-columns:1fr 1fr;column-gap:18px;row-gap:9px}
  .field{display:flex;align-items:flex-end;gap:4px;font-size:6px;color:var(--grey)}
  .field span.line{flex:1;border-bottom:1px solid var(--rule);height:8px}
  .fax-checks{position:absolute;left:22px;top:254px;width:292px;display:flex;justify-content:space-between;font-size:5.5px;color:var(--grey)}
  .check{display:flex;align-items:center;gap:3px}
  .check i{width:7px;height:7px;border:1px solid var(--grey)}

  /* envelopes */
  .envelope-back{left:732px;top:7px;width:460px;height:156px}
  .envelope-back .flap{position:absolute;inset:0}
  .seal{position:absolute;left:218px;top:30px;width:26px;height:26px;border-radius:50%;background:#d8dbe2}
  .envelope-under{left:732px;top:96px;width:460px;height:70px;background:var(--navy)}
  .envelope-front{left:740px;top:172px;width:452px;height:160px}
  .envelope-front .brand{left:18px;top:22px}
  .envelope-front .brand-name{font-size:12px}
  .envelope-front .contact{left:18px;top:48px}

  /* cards */
  .card-front{left:732px;top:367px;width:192px;height:125px}
  .card-front .brand{left:10px;top:12px}
  .card-front .brand-name{font-size:9px}
  .card-front .brand-dot{width:10px;height:10px}
  .card-front .contact{left:118px;top:34px;font-size:4.5px;line-height:6.5px}
  .card-back{left:948px;top:367px;width:192px;height:125px;background:var(--card-dark);display:flex;align-items:center;justify-content:center;gap:6px}
  .card-back .brand-dot{width:12px;height:12px;background:#8d9099}
  .card-back .brand-name{color:#8d9099;font-size:9px}
</style>
</head>
<body>

<section class="sheet letterhead">
  <div class="brand"><span class="brand-dot"></span><span class="brand-name">Varneth Systems</span></div>
  <div class="watermark"></div>
  <svg class="wave" viewBox="0 0 336 80" height="80" preserveAspectRatio="none">
    <path d="M0 44 C90 20 200 70 336 22" fill="none" stroke="var(--navy)" stroke-width="2"/>
    <path d="M0 50 C90 28 200 76 336 30 L336 80 L0 80Z" fill="var(--ink)"/>
  </svg>
  <p class="footer-text" style="right:16px;bottom:12px">418 W. Harrow Ln.<br>Kent, WA 98047<br>http://www.varneth.example</p>
</section>

<section class="sheet fax">
  <div class="brand"><span class="brand-dot"></span><span class="brand-name">Varneth Systems</span></div>
  <p class="contact">T 253.555.0147<br>F 253.555.0148<br>dorian.kelbrook@varneth.example</p>
  <h1 class="fax-title">FAX</h1>
  <div class="fax-fields">
    <div class="field">To:<span class="line"></span></div>
    <div class="field">From:<span class="line"></span></div>
    <div class="field">Fax:<span class="line"></span></div>
    <div class="field">Pages:<span class="line"></span></div>
    <div class="field">Phone:<span class="line"></span></div>
    <div class="field">Date:<span class="line"></span></div>
    <div class="field">Re:<span class="line"></span></div>
    <div class="field">CC:<span class="line"></span></div>
  </div>
  <div class="fax-checks">
    <span class="check"><i></i>Urgent</span>
    <span class="check"><i></i>For Review</span>
    <span class="check"><i></i>Please Comment</span>
    <span class="check"><i></i>Please Reply</span>
    <span class="check"><i></i>Please Recycle</span>
  </div>
  <svg class="wave" viewBox="0 0 336 80" height="80" preserveAspectRatio="none">
    <path d="M0 44 C90 20 200 70 336 22" fill="none" stroke="var(--navy)" stroke-width="2"/>
    <path d="M0 50 C90 28 200 76 336 30 L336 80 L0 80Z" fill="var(--ink)"/>
  </svg>
  <p class="footer-text" style="right:16px;bottom:24px">418 W. Harrow Ln. Kent, WA 98047</p>
  <p class="tagline" style="right:16px;bottom:10px">Providing Enterprise Business Solutions</p>
</section>

<div class="envelope envelope-under"></div>
<section class="envelope envelope-back">
  <svg class="flap" viewBox="0 0 460 156" preserveAspectRatio="none">
    <path d="M0 0 L230 70 L460 0" fill="none" stroke="#d5d8de" stroke-width="1"/>
  </svg>
  <div class="seal"></div>
</section>

<section class="envelope envelope-front">
  <div class="brand"><span class="brand-dot"></span><span class="brand-name">Varneth Systems</span></div>
  <p class="contact">418 W. Harrow Ln. Kent, WA 98047</p>
  <svg class="wave" viewBox="0 0 452 50" height="50" preserveAspectRatio="none">
    <path d="M0 30 C120 10 280 46 452 12" fill="none" stroke="var(--navy)" stroke-width="2"/>
    <path d="M0 35 C120 16 280 50 452 18 L452 50 L0 50Z" fill="var(--ink)"/>
  </svg>
</section>

<section class="card card-front">
  <div class="brand"><span class="brand-dot"></span><span class="brand-name">Varneth Systems</span></div>
  <p class="contact">Dorian Kelbrook<br>T 253.555.0147<br>dorian.kelbrook@varneth.example<br>www.varneth.example</p>
  <svg class="wave" viewBox="0 0 192 34" height="34" preserveAspectRatio="none">
    <path d="M0 20 C60 6 120 30 192 8" fill="none" stroke="var(--navy)" stroke-width="1.5"/>
    <path d="M0 24 C60 10 120 34 192 12 L192 34 L0 34Z" fill="var(--ink)"/>
  </svg>
</section>

<section class="card card-back">
  <span class="brand-dot"></span><span class="brand-name">Varneth</span>
</section>

</body>
</html>
```